Travel Company is looking for a STAND OUT Business Card

I need a unique Business Card that will truly stand out. Nothing too busy. Simple is good, right? Not looking for a standard design either. No cookie cutter layout. We are a Travel Company that works more with Companies than Travelers. I had an idea to focus and emphasis on the 2 logo a bit more. This is not necessary, however thought it would look interesting. I am just looking for something interesting and a bit different. Does't have to completely off the wall crazy, just not your run of the mill business card.

Target Market(s)

Hoteliers, Resort Management, Call Centers, Executives, Travelers, Families, Businesses

Industry/Entity Type

Hospitality

Contact Information for Business Card

President/CEO - Marcus T Bellamy (title not necessary if design doesn't allow for it)
contact - (407) 555-0186
email - mbellamy@wayfarenow.example
address - 4812 Quillmore Ave #164
Orlando, FL 32804
website - www.wayfarenow.example

Font styles to use
Serif
Other font styles liked:
• Avenir Next LT Pro BOLD

Requirements
Must have
• simple look and design. Unique design
Nice to have
• I attached the 2 logo separate from the main logo. This can be used separately from the Main Logo, together with the main logo or as main logo. I included the logo font. Use it or not, designers choice.
Should not have
• cookie cutter design. Little use of red other than the logo

```html
<!DOCTYPE html>
<html lang="en">
<head>
<meta charset="utf-8">
<title>Wayfare Now – Business Card</title>
<link rel="stylesheet" href="https://fonts.googleapis.com/css2?family=Source+Sans+3:wght@400;600;700&display=swap">
<style>
  :root {
    --backdrop: #3b3430;
    --card: #0d0d0d;
    --card-edge: #1c1c1c;
    --accent-red: #e5101a;
    --text-white: #f2f2f2;
    --silver: #b9b9b9;
  }
  * { box-sizing: border-box; margin: 0; padding: 0; }
  html, body {
    width: 1200px; height: 900px; overflow: hidden;
    background: var(--backdrop);
    font-family: "Source Sans 3", "Helvetica Neue", Arial, sans-serif;
  }
  .stage {
    width: 1200px; height: 900px;
    display: flex; align-items: center; justify-content: center; gap: 60px;
  }
  .card {
    width: 525px; height: 300px;
    background: var(--card);
    border: 1px solid var(--card-edge);
    box-shadow: 0 18px 40px rgba(0,0,0,.5);
    position: relative;
  }
  /* Contact side */
  .card-front { display: flex; align-items: center; }
  .brand-block {
    width: 215px; height: 100%;
    display: flex; align-items: center; justify-content: center; gap: 10px;
  }
  .brand-dot {
    width: 18px; height: 18px; border-radius: 50%;
    background: var(--accent-red);
  }
  .brand-name {
    color: var(--text-white);
    font-weight: 700; font-size: 24px; letter-spacing: .3px;
  }
  .divider {
    width: 1px; height: 130px;
    background: linear-gradient(to bottom, transparent, var(--accent-red), transparent);
  }
  .contact {
    padding-left: 26px; color: var(--text-white);
    font-size: 15px; line-height: 1.3;
  }
  .contact-name { color: var(--accent-red); font-weight: 700; font-size: 18px; }
  .contact-title { font-size: 14px; margin-bottom: 14px; }
  .contact-address { margin-bottom: 12px; }
  .contact-lines { list-style: none; }
  .contact-lines li { display: flex; align-items: center; gap: 8px; }
  .contact-lines svg { width: 11px; height: 11px; fill: var(--accent-red); flex: none; }
  /* Logo side */
  .card-back { display: flex; align-items: center; justify-content: center; gap: 14px; }
  .back-dot {
    width: 30px; height: 30px; border-radius: 50%;
    background: var(--silver);
  }
  .back-name {
    color: var(--silver); font-weight: 700; font-size: 52px; letter-spacing: -.5px;
  }
</style>
</head>
<body>
<main class="stage">
  <section class="card card-front" aria-label="Business card, contact side">
    <div class="brand-block">
      <span class="brand-dot"></span>
      <span class="brand-name">Wayfare Now</span>
    </div>
    <div class="divider"></div>
    <div class="contact">
      <p class="contact-name">Marcus T Bellamy</p>
      <p class="contact-title">President/CEO</p>
      <p class="contact-address">4812 Quillmore Ave #164<br>Orlando, FL 32804</p>
      <ul class="contact-lines">
        <li><svg viewBox="0 0 24 24"><path d="M6.6 10.8a15 15 0 0 0 6.6 6.6l2.2-2.2a1 1 0 0 1 1-.25 11.4 11.4 0 0 0 3.6.57 1 1 0 0 1 1 1V20a1 1 0 0 1-1 1A17 17 0 0 1 3 4a1 1 0 0 1 1-1h3.5a1 1 0 0 1 1 1c0 1.25.2 2.45.57 3.6a1 1 0 0 1-.25 1z"/></svg>(407) 555-0186</li>
        <li><svg viewBox="0 0 24 24"><path d="M2 5h20v14H2z M3 6l9 7 9-7" fill="var(--accent-red)"/><path d="M3 6l9 7 9-7" fill="none" stroke="#0d0d0d" stroke-width="2"/></svg>mbellamy@wayfarenow.example</li>
        <li><svg viewBox="0 0 24 24"><circle cx="12" cy="12" r="10"/></svg>www.wayfarenow.example</li>
      </ul>
    </div>
  </section>

  <section class="card card-back" aria-label="Business card, logo side">
    <span class="back-dot"></span>
    <span class="back-name">Wayfare Now</span>
  </section>
</main>
</body>
</html>
```